RMT Blazin' Riverdale, American Quarter Horse Stallion Stud Services

Advertisement for stud service. I'd like to showcase how stunningly beautiful this horse is with the full-body pic and how sweet, gentle, and quiet he is with the other pic. I want two-sided cards with photos on both sides. Headshot (cropped) on front with info on management, contact #s, etc. Full-body, datepair.example-type pic on back with some information on his pedigree. I'd like something striking enough that even if people don't want the service, they keep the card.

Target Market(s)

Horse owners, horse breeders, horse trainers, equestrians

Industry/Entity Type

Contact Information for Business Card

Horse's name: RMT Blazin' Riverdale
Owner: Norma Tillet
Manager: Cory Lindqvist
Phone: 208-555-0147
Pedigree information: Sire - Oaks Mon Pierrot, Dam - Bright Maned Lucerita
Sire's parents: Riverdale Dox 42 (sire) and Cedars Lovely Belle (dam)
Dam's parents: Shez Lucerita (sire) and Bright Maned Waltz (dam)

Font styles to use
Sans Serif

Requirements
Must have
• Rich, distinctive look. Should be a stand-out card; one that people keep even if they're not interested in the service.
Nice to have
• Pedigree information displayed in a family-tree arrangement. The horse is black, so I am picturing cards that are mostly black, probably with white or off-white (cream-colored) lettering. In fact, the horse has what's known as the cream-color gene, so maybe cream-colored would be better.

```html
<!DOCTYPE html>
<html lang="en">
<head>
<meta charset="utf-8">
<title>RMT Blazin' Riverdale – Business Card</title>
<link rel="stylesheet" href="https://fonts.googleapis.com/css2?family=Open+Sans:wght@400;700;800&display=swap">
<style>
  :root {
    --backdrop: #cdcfd2;
    --card-cream: #faf7ee;
    --spine: #4a4341;
    --label-tan: #c28d70;
    --ink: #111111;
    --photo-deep: #3e332e;
    --photo-mid: #7a6a60;
    --photo-sand: #d9d0c3;
  }
  * { margin: 0; padding: 0; box-sizing: border-box; }
  html, body {
    width: 1194px;
    height: 1200px;
    overflow: hidden;
    background: var(--backdrop);
    font-family: "Open Sans", Arial, sans-serif;
  }
  .business-card {
    position: absolute;
    left: 97px;
    top: 314px;
    width: 1000px;
    height: 572px;
    background: var(--card-cream);
    overflow: hidden;
    box-shadow: 0 6px 18px rgba(0,0,0,0.18);
  }
  .card-spine {
    position: absolute;
    left: 0;
    top: 0;
    width: 20px;
    height: 100%;
    background: var(--spine);
  }
  .horse-photo {
    position: absolute;
    right: 0;
    top: 0;
    width: 440px;
    height: 100%;
    background:
      linear-gradient(to right, var(--card-cream) 0%, rgba(250,247,238,0) 45%),
      linear-gradient(to bottom, rgba(62,51,46,0.05) 0%, rgba(217,208,195,0.6) 100%),
      radial-gradient(ellipse at 60% 35%, var(--photo-deep) 0%, var(--photo-mid) 55%, var(--photo-sand) 100%);
  }
  .contact-list {
    position: absolute;
    left: 67px;
    top: 62px;
    list-style: none;
  }
  .contact-item { margin-bottom: 36px; }
  .contact-label {
    display: block;
    font-size: 19px;
    line-height: 1.1;
    color: var(--label-tan);
  }
  .contact-value {
    display: block;
    font-size: 27px;
    line-height: 1.2;
    color: var(--ink);
  }
  .horse-name {
    position: absolute;
    left: 60px;
    top: 450px;
    font-size: 52px;
    font-weight: 800;
    letter-spacing: 1px;
    color: var(--ink);
    white-space: nowrap;
  }
</style>
</head>
<body>
  <section class="business-card">
    <div class="card-spine"></div>
    <div class="horse-photo" role="img" aria-label="Photo of the black stallion's head in a bridle, fading into the cream card"></div>
    <ul class="contact-list">
      <li class="contact-item">
        <span class="contact-label">owner</span>
        <span class="contact-value">Norma Tillet</span>
      </li>
      <li class="contact-item">
        <span class="contact-label">manager</span>
        <span class="contact-value">Cory Lindqvist</span>
      </li>
      <li class="contact-item">
        <span class="contact-label">phone</span>
        <span class="contact-value">208.555.0147</span>
      </li>
    </ul>
    <h1 class="horse-name">RMT Blazin’ Riverdale</h1>
  </section>
</body>
</html>
```